Trifold Business Brochure Design Project

Can you design a trifold brochure for my business? Suggested material for each of the 6 panels is in the attached document, My logo is also attached (from print haven), and info on my website, derek@dereklhcpa.com. Colors to match my logo. Theme the same as my logo, an outdoor/mountain/river, etc feel.

Target Market(s)

Business owners

Requirements
Nice to have
• See attached

```html
<!DOCTYPE html>
<html lang="en">
<head>
<meta charset="utf-8">
<title>Derek Lander CPA — Trifold Brochure</title>
<link href="https://fonts.googleapis.com/css2?family=Montserrat:wght@400;500;600;700;800&display=swap" rel="stylesheet">
<style>
:root{
  --page:#eceef2;
  --forest:#44573f;
  --forest-deep:#2f3d2c;
  --lime:#bfd869;
  --ink:#253022;
  --body:#3b4538;
  --white:#ffffff;
  --mist:#e4e6e4;
}
*{margin:0;padding:0;box-sizing:border-box}
html,body{width:833px;height:1200px;overflow:hidden;background:var(--page)}
body{position:relative;font-family:"Montserrat",sans-serif;color:var(--ink)}
.spread{
  position:absolute;left:57px;width:1376px;height:972px;background:var(--white);
  transform:scale(0.5225);transform-origin:0 0;overflow:hidden;
  box-shadow:0 6px 18px rgba(0,0,0,.08);
}
.spread--outside{top:62px}
.spread--inside{top:632px}
.shapes{position:absolute;inset:0;width:1376px;height:972px}
.block{position:absolute}
.heading{font-weight:700;font-size:32px;line-height:38px;color:var(--forest);letter-spacing:.3px}
.heading--ink{color:var(--ink)}
.bar{display:block;width:70px;height:6px;border-radius:3px;background:var(--lime);margin-top:10px}
.bar--ink{background:var(--ink)}
.bar--white{background:var(--white)}
.copy{font-size:15.5px;line-height:24.5px;color:var(--body);text-align:justify}
.copy + .copy{margin-top:24px}

/* outside */
.about{left:55px;top:418px;width:350px}
.about .copy:first-of-type{margin-top:38px}
.quote{left:513px;top:218px;color:var(--white);font-size:27px;line-height:33px;font-weight:500;letter-spacing:.5px}
.quote .bar{margin-top:18px}
.contact{left:512px;top:622px}
.contact dl{margin-top:26px}
.contact dt{font-size:18px;font-weight:600;color:var(--ink);line-height:24px}
.contact dd{font-size:18px;font-weight:400;color:var(--ink);line-height:24px;margin-bottom:14px}
.brandmark{left:1000px;top:92px;display:flex;align-items:center;gap:8px;font-size:15px;font-weight:700;color:var(--forest)}
.brandmark .dot{width:12px;height:12px;border-radius:50%;background:var(--lime)}
.cover-title{left:972px;top:718px;color:var(--forest);font-weight:700}
.cover-title .small{font-size:32px;line-height:40px}
.cover-title .big{font-size:48px;line-height:50px;font-weight:800}
.cover-title .bar{margin-top:12px}
.tagline{left:972px;top:888px;font-size:16.5px;font-weight:600;color:var(--ink)}

/* inside */
.promise{left:513px;top:126px;color:var(--white)}
.promise .lead{font-size:22px;font-weight:500;letter-spacing:.5px}
.promise .big{font-size:34px;line-height:39px;font-weight:800;margin-top:14px}
.features{left:972px;top:50px;width:350px}
.features .copy{margin-top:30px}
.services{left:55px;top:356px;width:350px}
.services .copy{margin-top:22px;text-align:justify;color:var(--forest)}
.service-list{list-style:none;position:absolute;left:55px;top:0}
.service-list li{position:absolute;left:0;width:380px;display:flex;align-items:center;gap:22px;font-size:15px;font-weight:700;line-height:22px;color:var(--forest);transform:translateY(-50%)}
.service-list svg{flex:none}
.why{left:512px;top:604px;width:360px}
.why .copy{margin-top:22px;text-align:left;color:var(--forest)}
.why-list{list-style:none;position:absolute;left:512px;top:0}
.why-list li{position:absolute;left:0;width:320px;display:flex;align-items:center;gap:26px;font-size:17px;font-weight:700;color:var(--forest);transform:translateY(-50%)}
</style>
</head>
<body>

<section class="spread spread--outside" aria-label="Brochure outside">
  <svg class="shapes" viewBox="0 0 1376 972" aria-hidden="false">
    <defs>
      <linearGradient id="deskTone" x1="0" y1="0" x2="1" y2="1">
        <stop offset="0" stop-color="#9fbf4e"/>
        <stop offset=".55" stop-color="#b9c85a"/>
        <stop offset="1" stop-color="#7d8d3c"/>
      </linearGradient>
      <linearGradient id="officeTone" x1="0" y1="0" x2="1" y2="1">
        <stop offset="0" stop-color="#6f7a6c"/>
        <stop offset=".5" stop-color="#3b4a3a"/>
        <stop offset="1" stop-color="#283427"/>
      </linearGradient>
    </defs>
    <polygon points="0,0 459,0 459,437 0,210" fill="url(#deskTone)" role="img" aria-label="Photo: business meeting with laptop and tablet on a desk"/>
    <path d="M0,262 L90,305 Q100,317 90,328 L0,373 Z" fill="var(--forest)"/>
    <path d="M459,0 L1000,252 L1376,55 L1376,470 L975,665 Q947,680 915,665 L459,437 Z" fill="var(--forest)"/>
    <path d="M1150,108 L1376,232 L1376,512 L1152,630 L918,500 L918,238 Z" fill="var(--mist)" opacity=".55"/>
    <path d="M1150,118 L1376,242 L1376,502 L1152,620 L928,494 L928,244 Z" fill="url(#officeTone)" role="img" aria-label="Photo: smiling accountant at a laptop in a bright office"/>
    <polygon points="808,79 860,42 860,114" fill="var(--lime)"/>
    <polygon points="1376,570 1300,625 1376,677" fill="var(--lime)"/>
    <polygon points="513,539 555,567 513,594" fill="#eeefee"/>
  </svg>

  <div class="block brandmark"><span class="dot"></span>Derek Lander CPA</div>

  <div class="block quote">
    <p>“LOREM IPSUM<br>AMEI CONCTETUR<br>ADIYSED&nbsp; EIUSMOD<br>TEMPOR ICIDIDUNT”</p>
    <span class="bar bar--white"></span>
  </div>

  <div class="block about">
    <h2 class="heading">ABOUT US</h2>
    <span class="bar"></span>
    <p class="copy">Lorem ipsum dolor amet consectetu adipisicin elised do eiusmod tempor incididunt ut labore dolore magna aliqua.</p>
    <p class="copy">Utenim minim veniaquis nostrud and exertion ullamco laboris nisiut aliquip this commodo consequat. Duis auteir dolor repreh enderit voluptate velit esse cillum dolore fugiat nulla pariatur. Excepteur occaecat cupidatat thisn proident sunt culpa qui officia deserunt mollit anim est laborum. Sed perspiciatis unde omnis natu voluptatem accusantium repreh enderit voluptate velit esse cillum dolore fugiat nulla pariatur. Excepteur occaecat cupidatat thisn proident sunt culpa. Sed perspiciatis unde omnis natu voluptatem accusantium repreh enderit voluptate velitth.</p>
  </div>

  <div class="block contact">
    <h2 class="heading">GET IN TOUCH</h2>
    <span class="bar"></span>
    <dl>
      <dt>Phone</dt><dd>555.210.4478</dd>
      <dt>Fax</dt><dd>555.210.4490</dd>
      <dt>Email</dt><dd>derek@dereklhcpa.com</dd>
      <dt>Web</dt><dd>https://dereklhcpa.com</dd>
    </dl>
  </div>

  <div class="block cover-title">
    <p class="small">DEREK</p>
    <p class="big">DEREK</p>
    <p class="small">CPA</p>
    <span class="bar"></span>
  </div>
  <p class="block tagline">Your Fractional CFO and so much more</p>
</section>

<section class="spread spread--inside" aria-label="Brochure inside">
  <svg class="shapes" viewBox="0 0 1376 972">
    <defs>
      <linearGradient id="roomTone" x1="0" y1="0" x2="1" y2="1">
        <stop offset="0" stop-color="#dde2e6"/>
        <stop offset=".6" stop-color="#b7bfc6"/>
        <stop offset="1" stop-color="#3e4d66"/>
      </linearGradient>
      <linearGradient id="teamTone" x1="0" y1="0" x2="1" y2="1">
        <stop offset="0" stop-color="#3e4d3b"/>
        <stop offset="1" stop-color="#2c3a2a"/>
      </linearGradient>
      <linearGradient id="growthTone" x1="0" y1="1" x2="1" y2="0">
        <stop offset="0" stop-color="#8c8a7a"/>
        <stop offset=".6" stop-color="#c9cfcf"/>
        <stop offset="1" stop-color="#4fb8b4"/>
      </linearGradient>
    </defs>
    <polygon points="1376,452 1376,972 650,972" fill="url(#growthTone)" role="img" aria-label="Photo: hands on a laptop with a rising growth chart"/>
    <path d="M0,175 L916,605 L1150,762 Q1172,780 1150,796 L650,972 L0,972 Z" fill="var(--lime)"/>
    <polygon points="0,0 459,0 459,380 0,162" fill="url(#roomTone)" role="img" aria-label="Photo: two consultants reviewing documents"/>
    <path d="M459,0 L916,0 L916,560 Q916,598 880,592 L459,395 Z" fill="url(#teamTone)" role="img" aria-label="Photo: office desk scene with plant, tinted green"/>
  </svg>

  <div class="block promise">
    <p class="lead">WE ARE HERE TO</p>
    <p class="big">HELP<br>GROW YOUR<br>BUSINESS</p>
  </div>

  <div class="block features">
    <h2 class="heading">OUR<br>FEATURES</h2>
    <span class="bar"></span>
    <p class="copy">Lorem ipsum dolor sit amet, consectetur adipisicing elit, sed do eiusmod tempor incididunt ut labore et dolore magna aliqua. Ut enim ad minim veniam, quis nostrud exercitation ullamco laboris nisi ut aliquip ex ea commodo consequat. Duis aute irure dolor in reprehenderit in voluptate velit esse cillum dolore eu fugiat nulla pariatur. Excepteur sint occaecat cupidatat non proident, sunt in culpa qui officia deserunt mollit anim id est laborum. Sed ut perspiciatis unde omnis iste natus error sit voluptatem accusantium doloremque laudantium totarem.</p>
  </div>

  <div class="block services">
    <h2 class="heading heading--ink">OUR SERVICES</h2>
    <span class="bar bar--ink"></span>
    <p class="copy">Lorem ipsum dolor sit amet, consectetur adipisicing elit, sed do eiusmod tempor incididunt ut labore et dolore magna aliqua</p>
  </div>

  <ul class="service-list">
    <li style="top:542px"><svg width="28" height="28" viewBox="0 0 28 28"><circle cx="14" cy="14" r="12.5" fill="none" stroke="var(--forest)" stroke-width="2"/><path d="M8.5,14.5 L12.5,18.5 L19.5,9.5" fill="none" stroke="var(--forest)" stroke-width="2.4" stroke-linecap="round" stroke-linejoin="round"/></svg><span>FRACTIONAL CFO/CONTROLLER<br>SERVICES</span></li>
    <li style="top:597px"><svg width="28" height="28" viewBox="0 0 28 28"><circle cx="14" cy="14" r="12.5" fill="none" stroke="var(--forest)" stroke-width="2"/><path d="M8.5,14.5 L12.5,18.5 L19.5,9.5" fill="none" stroke="var(--forest)" stroke-width="2.4" stroke-linecap="round" stroke-linejoin="round"/></svg><span>FINANCIAL/CASH FLOW<br>PROJECTIONS</span></li>
    <li style="top:642px"><svg width="28" height="28" viewBox="0 0 28 28"><circle cx="14" cy="14" r="12.5" fill="none" stroke="var(--forest)" stroke-width="2"/><path d="M8.5,14.5 L12.5,18.5 L19.5,9.5" fill="none" stroke="var(--forest)" stroke-width="2.4" stroke-linecap="round" stroke-linejoin="round"/></svg><span>BUSINESS EXIT PLANNING</span></li>
    <li style="top:680px"><svg width="28" height="28" viewBox="0 0 28 28"><circle cx="14" cy="14" r="12.5" fill="none" stroke="var(--forest)" stroke-width="2"/><path d="M8.5,14.5 L12.5,18.5 L19.5,9.5" fill="none" stroke="var(--forest)" stroke-width="2.4" stroke-linecap="round" stroke-linejoin="round"/></svg><span>BUSINESS VALUE CREATION</span></li>
    <li style="top:719px"><svg width="28" height="28" viewBox="0 0 28 28"><circle cx="14" cy="14" r="12.5" fill="none" stroke="var(--forest)" stroke-width="2"/><path d="M8.5,14.5 L12.5,18.5 L19.5,9.5" fill="none" stroke="var(--forest)" stroke-width="2.4" stroke-linecap="round" stroke-linejoin="round"/></svg><span>INDUSTRY KPIS &amp; BENCHMARKING</span></li>
    <li style="top:757px"><svg width="28" height="28" viewBox="0 0 28 28"><circle cx="14" cy="14" r="12.5" fill="none" stroke="var(--forest)" stroke-width="2"/><path d="M8.5,14.5 L12.5,18.5 L19.5,9.5" fill="none" stroke="var(--forest)" stroke-width="2.4" stroke-linecap="round" stroke-linejoin="round"/></svg><span>LABOR ANALYSIS</span></li>
    <li style="top:795px"><svg width="28" height="28" viewBox="0 0 28 28"><circle cx="14" cy="14" r="12.5" fill="none" stroke="var(--forest)" stroke-width="2"/><path d="M8.5,14.5 L12.5,18.5 L19.5,9.5" fill="none" stroke="var(--forest)" stroke-width="2.4" stroke-linecap="round" stroke-linejoin="round"/></svg><span>TAX PLANNING</span></li>
    <li style="top:838px"><svg width="28" height="28" viewBox="0 0 28 28"><circle cx="14" cy="14" r="12.5" fill="none" stroke="var(--forest)" stroke-width="2"/><path d="M8.5,14.5 L12.5,18.5 L19.5,9.5" fill="none" stroke="var(--forest)" stroke-width="2.4" stroke-linecap="round" stroke-linejoin="round"/></svg><span>INTERNAL CONTROL/AUDIT<br>CONSULTING</span></li>
    <li style="top:880px"><svg width="28" height="28" viewBox="0 0 28 28"><circle cx="14" cy="14" r="12.5" fill="none" stroke="var(--forest)" stroke-width="2"/><path d="M8.5,14.5 L12.5,18.5 L19.5,9.5" fill="none" stroke="var(--forest)" stroke-width="2.4" stroke-linecap="round" stroke-linejoin="round"/></svg><span>SYSTEM CONVERSIONS</span></li>
    <li style="top:918px"><svg width="28" height="28" viewBox="0 0 28 28"><circle cx="14" cy="14" r="12.5" fill="none" stroke="var(--forest)" stroke-width="2"/><path d="M8.5,14.5 L12.5,18.5 L19.5,9.5" fill="none" stroke="var(--forest)" stroke-width="2.4" stroke-linecap="round" stroke-linejoin="round"/></svg><span>ACCOUNTING SERVICES</span></li>
  </ul>

  <div class="block why">
    <h2 class="heading heading--ink">WHY CHOOSE US</h2>
    <span class="bar bar--ink"></span>
    <p class="copy">Lorem&nbsp; doloramet, consectetur adipisicing do eiusmod tempor incididunt ut labore et dolore magna aliqua enim adminim</p>
  </div>

  <ul class="why-list">
    <li style="top:785px"><svg width="24" height="24" viewBox="0 0 24 24"><path d="M21,3 L3,10.5 L10,13.5 L13,21 Z M10,13.5 L21,3" fill="none" stroke="var(--forest)" stroke-width="1.8" stroke-linejoin="round"/></svg><span>LOREM IPSUM DOLOR</span></li>
    <li style="top:827px"><svg width="24" height="24" viewBox="0 0 24 24"><path d="M4,10 L4,15 L8,15 L16,19 L16,6 L8,10 Z M8,15 L9.5,20 L12,20 L11,16.2 M19,10 L19,15" fill="none" stroke="var(--forest)" stroke-width="1.8" stroke-linejoin="round" stroke-linecap="round"/></svg><span>DOLOR SIT AMET</span></li>
    <li style="top:869px"><svg width="24" height="24" viewBox="0 0 24 24"><path d="M12,6 A5,5 0 0 1 15,15 L15,17.5 L9,17.5 L9,15 A5,5 0 0 1 12,6 Z M9.5,20.5 L14.5,20.5 M12,1.5 L12,3 M4,9.5 L5.5,10 M20,9.5 L18.5,10 M6,4 L7,5.2 M18,4 L17,5.2" fill="none" stroke="var(--forest)" stroke-width="1.6" stroke-linecap="round" stroke-linejoin="round"/></svg><span>LOREM IPSUM DOLOR</span></li>
  </ul>
</section>

</body>
</html>
```